Travesco Business Cards

We need a business card design for Travesco Mining.

This is a B2B company that buys and sells large machinery tires within the coal mining industry. The design should the strong, crisp and masculine. I have uploaded the company logo and rough mock-up of what the back of the card should look like. the front of the card should have the same look/feel as the back. I need editable templates for both the front and the back of the card.

Color scheme should be grey/green/black

Contact information to include on the card:
Name: Dale Pemberton
Title: Managing Director
Phone: 214-503-6192
Address: 1185 Wexley #3 Dallas, TX 75211
Email: Dale@Travesco-example.com

I am also opening a contest for letterhead design. If you submit a business card design, please also submit a letterhead design with the same look/feel. The winner of the business card design will also will the letter head and be paid for both.

Target Market(s)

Procurement men/women in the coal mining industry

Industry/Entity Type

Coal Mining

```html
<!DOCTYPE html>
<html lang="en">
<head>
<meta charset="utf-8">
<title>Travesco Mining – Business Cards</title>
<link rel="stylesheet" href="https://fonts.googleapis.com/css2?family=Roboto:wght@400;500&display=swap">
<style>
  :root {
    --stage: #646464;
    --card-dark: #000000;
    --card-light: #ffffff;
    --green: #5aa532;
    --band-dark: #2a2a2b;
    --band-light: #58595b;
    --ink: #3a3a3c;
    --muted: #a7a8aa;
    --white: #ffffff;
  }
  * { box-sizing: border-box; margin: 0; padding: 0; }
  html, body {
    width: 1200px;
    height: 392px;
    overflow: hidden;
    background: var(--stage);
    font-family: "Roboto", Arial, sans-serif;
  }
  .stage { position: relative; width: 1200px; height: 392px; }
  .card {
    position: absolute;
    top: 42px;
    width: 476px;
    height: 307px;
    overflow: hidden;
  }
  .card--back { left: 142px; background: var(--card-dark); }
  .card--front { left: 679px; background: var(--card-light); }

  /* plain graphic bands */
  .band { position: absolute; }
  .card--back .band--top { left: 0; top: 0; width: 120px; height: 84px; background: var(--band-dark); }
  .card--back .band--side { left: 0; top: 116px; width: 165px; height: 191px; background: var(--band-dark); }
  .card--front .band--top { left: 30px; top: 0; width: 160px; height: 84px; background: var(--green); }
  .card--front .band--side { left: 0; top: 116px; width: 190px; height: 191px; background: var(--band-light); }

  .brand {
    position: absolute;
    display: flex;
    align-items: center;
    gap: 10px;
  }
  .brand__square {
    width: 22px;
    height: 22px;
    background: var(--green);
    flex: none;
  }
  .brand__name {
    font-weight: 500;
    font-size: 24px;
    letter-spacing: 1px;
    text-transform: uppercase;
    line-height: 1;
    white-space: nowrap;
  }
  .card--back .brand { left: 180px; top: 240px; }
  .card--back .brand__name { color: var(--white); }
  .card--front .brand { left: 214px; top: 48px; }
  .card--front .brand__name { color: var(--ink); font-size: 21px; }

  .contact {
    position: absolute;
    left: 214px;
    top: 136px;
    font-size: 14.5px;
    line-height: 18px;
    letter-spacing: 0.3px;
  }
  .contact__name { color: var(--ink); }
  .contact__title { color: var(--green); margin-bottom: 9px; }
  .contact__line { color: var(--muted); }
  .contact__indent { padding-left: 67px; }
</style>
</head>
<body>
  <main class="stage">
    <section class="card card--back" aria-label="Card back">
      <div class="band band--top"></div>
      <div class="band band--side"></div>
      <div class="brand">
        <span class="brand__square"></span>
        <span class="brand__name">Travesco Mining</span>
      </div>
    </section>

    <section class="card card--front" aria-label="Card front">
      <div class="band band--top"></div>
      <div class="band band--side"></div>
      <div class="brand">
        <span class="brand__square"></span>
        <span class="brand__name">Travesco Mining</span>
      </div>
      <div class="contact">
        <p class="contact__name">Dale Pemberton</p>
        <p class="contact__title">Managing Director</p>
        <p class="contact__line">Phone: 214-503-6192</p>
        <p class="contact__line">Address: 1185 Wexley #3 Dallas,</p>
        <p class="contact__line contact__indent">TX 75211</p>
        <p class="contact__line">Email: Dale@Travesco-example.com</p>
      </div>
    </section>
  </main>
</body>
</html>
```